Integrative Medical Practice Website Redo

I am needing to have our current website redesigned to make it a responsive website to work on smartphones.
Current website
www.brightoakfm.com
Here are several examples of what I am looking for
https://www.thymecarehub.com/
I am wanting a popup for a newsletter signup
Looking for a very professional, clean, simple, minimalist, bold well designed website
Colors would ideally be greens and blues, cool tones, muted colors, or graytones like:
https://journeybalance.org/
Several other clean design examples
http://9anchorsboulder.com/
http://www.velumedical.com/
http://sproutyouth.com/
http://ourcellcastle.com/
I would like the top navigation bar to be able to slide down while browsing site
We are also needing to add several features that are not on our current website:
Questionnaire buttons
Are you toxic questionnaire?
Take our hormone quiz to find out if hormones are affecting your health.
online scheduling option for:
nutrition counselling
testing like body composition, basal metabolic rate, CIMT, breast thermography, VO2 Max testing, Vita Beat
Therapies like whole body vibration, infrared sauna, Exercise with oxygen, hyperbaric oxygen, spinal decompression
Need to have separate page for different services and split up services into:
Consults/Office Visits, Testing, Therapies, Procedures
Need to have a button link to patient portal
Needs to have online store
Need to add navigation button "Start Here"
Need a spot for a video on practice summary
Newsletter signup to collect emails
Testimonials from facebook
Blog that posts can be shared with social media
Password protected patient access that can integrate into crate.io ideally
Modules for programs online classes/videos
I have attached stock images that you can use, but feel free to find others to use.
I have also attached a copy of our current brochure that shows an overview of the practice
Target Market(s)
Health conscious people of all ages looking for a family medicine doctor
Industry/Entity Type
Alternative Medicine
Coding
Coded - Design and coding required
Number of Pages Required
5+ page

```html
<!DOCTYPE html>
<html lang="en">
<head>
<meta charset="utf-8">
<title>Bright Oak Family Medicine</title>
<link href="https://fonts.googleapis.com/css2?family=Roboto:wght@400;500;700&family=Lato:wght@400;700&display=swap" rel="stylesheet">
<style>
:root{
  --green:#7cbf3f;
  --green-dark:#5fa12a;
  --blue:#1f73a8;
  --cyan:#1aa6d9;
  --teal:#2a7fa3;
  --ink:#222;
  --text:#777;
  --muted:#9a9a9a;
  --line:#e3e3e3;
  --grey-bg:#f2f2f2;
  --footer:#2f2f2f;
  --white:#fff;
  --red:#e23b3b;
}
*{box-sizing:border-box;margin:0;padding:0}
html,body{width:1200px;height:3557px;overflow:hidden}
body{font-family:"Lato",sans-serif;color:var(--text);background:var(--white);font-size:12px;line-height:1.6}
h1,h2,h3,h4{font-family:"Roboto",sans-serif;color:var(--ink);font-weight:500}
.container{width:704px;margin:0 auto;position:relative}
.section-title{text-align:center;font-size:34px;font-weight:500;color:var(--ink)}
.section-title::after{content:"";display:block;width:70px;height:2px;background:var(--green);margin:10px auto 0}
.btn{display:inline-block;border:1px solid #555;background:var(--white);color:var(--ink);font-size:11px;font-weight:700;padding:8px 16px;font-family:"Lato",sans-serif}
.btn-small{border:1px solid var(--teal);color:var(--teal);font-size:10px;padding:6px 18px;font-weight:400}
.btn-small.active{background:var(--teal);color:var(--white)}

/* header */
.site-header{height:88px;position:relative;background:var(--white)}
.top-strip{position:absolute;right:0;top:0;height:30px;width:748px;background:var(--green);display:flex;justify-content:flex-end;align-items:center;gap:22px;padding-right:252px;font-size:10px;color:var(--white)}
.top-strip::before{content:"";position:absolute;left:-30px;top:0;border-top:30px solid var(--green);border-left:30px solid transparent}
.brand{position:absolute;left:256px;top:12px;display:flex;align-items:center;gap:8px}
.brand-dot{width:22px;height:22px;border-radius:50%;background:var(--teal)}
.brand-name{font-family:"Roboto",sans-serif;font-size:24px;font-weight:500;color:var(--teal);line-height:1}
.brand-sub{font-size:9px;letter-spacing:3px;color:var(--teal);display:block;margin-top:3px}
.main-nav{position:absolute;left:474px;top:44px;display:flex;gap:17px;font-size:12px;color:#555;align-items:center}
.main-nav .current{border:1px solid var(--teal);color:var(--teal);padding:2px 6px}
.main-nav .start{border:1px solid var(--teal);color:var(--teal);padding:2px 10px;margin-left:18px;font-size:11px}

/* hero */
.hero{height:403px;position:relative;background:linear-gradient(90deg,#c9b3a3 0%,#e9e4df 35%,#eef2f2 60%,#f4f6f5 100%)}
.hero-photo{position:absolute;inset:0}
.hero-copy{position:absolute;left:560px;top:92px;text-align:center;width:380px}
.hero-copy h1{color:var(--blue);font-size:36px;font-weight:500;line-height:1.25}
.hero-brand{margin-top:18px;font-family:"Roboto",sans-serif;font-size:50px;font-weight:500;color:var(--teal);line-height:1}
.hero-brand small{display:block;font-size:16px;letter-spacing:6px;margin-top:6px}
.arrow{position:absolute;width:26px;height:26px;border-radius:50%;display:flex;align-items:center;justify-content:center;z-index:2}
.hero .arrow{top:276px;background:var(--cyan)}
.hero .arrow.prev{left:234px}
.hero .arrow.next{left:938px;background:var(--blue)}

/* welcome */
.welcome{height:320px;padding-top:52px;text-align:center}
.welcome p{margin:30px auto 24px;width:652px;font-size:10.5px;line-height:2.1;color:var(--muted)}

/* services */
.services{height:702px;background:var(--grey-bg);padding-top:36px;text-align:center}
.service-grid{display:grid;grid-template-columns:1fr 1fr;margin-top:70px;row-gap:58px}
.service{width:230px;margin:0 auto}
.service svg{display:block;margin:0 auto 10px}
.service h3{font-size:14px;font-weight:500;margin-bottom:8px}
.service p{font-size:9.5px;color:var(--muted);line-height:1.55;margin-bottom:14px}
.services .all{margin-top:70px}

/* questionnaire */
.quiz{height:308px;position:relative;background:linear-gradient(180deg,#8cc84b,#76bb3b);color:var(--white);text-align:center;padding-top:60px}
.quiz h2{color:var(--white);font-size:40px;font-weight:400}
.quiz p{font-family:"Roboto",sans-serif;font-size:22px;line-height:1.25;margin:10px auto 22px;width:660px}
.quiz .btn{background:transparent;border:2px solid var(--white);color:var(--white)}

/* products */
.products{height:391px;padding-top:71px;text-align:center;position:relative}
.product-row{display:flex;gap:24px;justify-content:center}
.product{width:157px;height:213px;background:var(--white);box-shadow:0 2px 8px rgba(0,0,0,.15);padding:18px 14px}
.product-img{height:120px;background:linear-gradient(180deg,#eaeaea,#cfcfcf);margin:0 18px}
.product .name{font-size:9px;color:var(--muted);margin-top:12px}
.product .price{font-family:"Roboto",sans-serif;font-size:14px;color:#444}
.product .price.sale{color:var(--red)}
.product .price s{font-size:9px;color:var(--muted);margin-left:4px}
.products .arrow{top:165px;background:var(--cyan)}
.products .arrow.prev{left:234px}
.products .arrow.next{left:938px;background:var(--blue)}
.products .btn{margin-top:36px}

/* reviews */
.reviews{height:406px;position:relative;background:linear-gradient(90deg,#e8e9e6,#f1f1ef 50%,#e4e7e1);text-align:center;padding-top:30px}
.reviews .container{z-index:1}
.avatar{width:104px;height:104px;border-radius:50%;border:5px solid var(--green);background:linear-gradient(160deg,#b98b70,#6b4b3d);margin:36px auto 14px}
.reviewer{font-size:9px;font-weight:700;letter-spacing:1px;color:#444}
.reviews blockquote{width:420px;margin:18px auto 0;font-size:14px;color:#a6a6a6;line-height:1.5}
.dots{display:flex;gap:7px;justify-content:center;margin-top:18px}
.dots span{width:9px;height:9px;border-radius:50%;background:#aaa}
.dots span.on{background:#444}

/* newsletter */
.newsletter{height:132px;background:var(--teal);display:flex;align-items:center;justify-content:center;gap:40px;padding-right:20px}
.newsletter h3{color:var(--white);font-size:17px;font-weight:500}
.newsletter p{color:#d8ecf5;font-size:8px;line-height:1.4;width:180px}
.signup{display:flex}
.signup span{width:150px;height:34px;border:1px solid #9fc7da;color:#d8ecf5;font-size:9px;padding:10px}
.signup b{height:34px;background:var(--white);color:var(--teal);font-size:9px;padding:11px 12px}

/* blogs */
.blogs{height:468px;padding-top:28px;text-align:center}
.blog-row{display:flex;gap:14px;margin-top:40px;text-align:left}
.post{width:225px}
.post-img{height:161px}
.post h4{color:var(--cyan);font-size:12px;font-weight:500;margin:10px 0 6px}
.post .date{font-size:8.5px;color:var(--muted);display:flex;align-items:center;gap:4px}
.post p{font-size:8.5px;color:#555;line-height:1.5;margin-top:6px}
.blogs .btn{margin-top:34px}

/* footer */
.site-footer{height:310px;background:var(--footer);color:#bbb}
.footer-grid{display:grid;grid-template-columns:310px 210px 184px;padding-top:72px}
.footer-brand{font-family:"Roboto",sans-serif;font-size:28px;color:#cfcfcf;font-weight:500;display:flex;align-items:center;gap:8px}
.footer-brand .brand-dot{background:#777;width:18px;height:18px}
.footer-about{font-size:10px;color:#eee;line-height:1.4;margin:14px 0 18px;width:230px}
.social{display:flex;gap:14px}
.social span{width:12px;height:12px;border-radius:50%;border:1px solid #999}
.site-footer h4{color:var(--white);font-size:12px;margin-top:-50px;margin-bottom:14px}
.recent{display:flex;gap:8px;margin-bottom:14px;align-items:center}
.recent i{width:32px;height:32px;background:linear-gradient(135deg,#5a8bb0,#c8d6e2)}
.recent b{color:var(--white);font-size:9px;display:block}
.recent small{font-size:8px}
.contact li{list-style:none;display:flex;gap:8px;font-size:8.5px;margin-bottom:10px;line-height:1.4}
.copyright{height:29px;background:var(--green);color:var(--white);font-size:9px;text-align:center;line-height:29px}
</style>
</head>
<body>

<header class="site-header">
  <div class="top-strip"><span>Wellness Membership</span><span>FAQ</span><span>Contact us</span></div>
  <div class="brand">
    <span class="brand-dot"></span>
    <div><span class="brand-name">Bright Oak</span><span class="brand-sub">FAMILY MEDICINE</span></div>
  </div>
  <nav class="main-nav">
    <span class="current">Home</span><span>About us</span><span>Services</span><span>Resources</span><span>Current Patients</span><span>New Patients</span><span class="start">START HERE</span>
  </nav>
</header>

<section class="hero">
  <div class="hero-photo" role="img" aria-label="Smiling woman in a red top holding a cup in a bright clinic"></div>
  <div class="hero-copy">
    <h1>WE Will Help<br>You To Make life Happy</h1>
    <div class="hero-brand">Bright Oak<small>FAMILY MEDICINE</small></div>
  </div>
  <span class="arrow prev"><svg width="10" height="10" viewBox="0 0 10 10"><path d="M6.5 1.5 3 5l3.5 3.5" fill="none" stroke="#fff" stroke-width="1.6"/></svg></span>
  <span class="arrow next"><svg width="10" height="10" viewBox="0 0 10 10"><path d="M3.5 1.5 7 5 3.5 8.5" fill="none" stroke="#fff" stroke-width="1.6"/></svg></span>
</section>

<section class="welcome">
  <div class="container">
    <h2 class="section-title">Welcome to Bright Oak</h2>
    <p>Welcome to our website. As an integrative medical practice, we provide innovative, quality family health care by uniquely combining both conventional and alternative medicine. Our aim is to treat the whole patient not just the symptoms. This "best of both worlds" approach provides patients with options in the management of their concerns while addressing the underlying cause of their illness. And as a primary care practice, we offer treatment for both acute and chronic conditions while emphasizing prevention, education and optimal health.</p>
    <span class="btn">Read More About Bright Oak</span>
  </div>
</section>

<section class="services">
  <div class="container">
    <h2 class="section-title">Our Some Services</h2>
    <div class="service-grid">
      <div class="service">
        <svg width="24" height="24" viewBox="0 0 24 24"><rect x="3" y="8" width="18" height="8" rx="4" transform="rotate(-35 12 12)" fill="none" stroke="#2a7fa3" stroke-width="2"/><path d="M9 7l6 10" stroke="#2a7fa3" stroke-width="2"/></svg>
        <h3>Family Medicine</h3>
        <p>In addition to what you would expect in primary family medicine, we offer many different modalities in our attempt to improve your quality of health, whether it is pharmaceutical or nutraceutical.</p>
        <span class="btn btn-small">Read More</span>
      </div>
      <div class="service">
        <svg width="24" height="24" viewBox="0 0 24 24"><path d="M12 7c-3-2-8-1-8 5s4 10 8 8c4 2 8-2 8-8s-5-7-8-5z" fill="none" stroke="#2a7fa3" stroke-width="2"/><path d="M12 7c0-2 1-4 3-4" fill="none" stroke="#2a7fa3" stroke-width="2"/></svg>
        <h3>Nutrition</h3>
        <p>Having a bachelor's degree in Nutritional Science, the doctor has the conviction that nutrition is one of the keys to optimal health, since nutrition affects every body system.</p>
        <span class="btn btn-small active">Read More</span>
      </div>
      <div class="service">
        <svg width="24" height="24" viewBox="0 0 24 24"><path d="M8 4v16M12 3v17M16 4v16" stroke="#2a7fa3" stroke-width="1.6" transform="rotate(-20 12 12)"/></svg>
        <h3>Acupuncture</h3>
        <p>Medical acupuncture provides many types of approaches that are used depending on the individual and their needs, such as pain management, energy balancing or treating a systemic condition.</p>
        <span class="btn btn-small">Read More</span>
      </div>
      <div class="service">
        <svg width="24" height="24" viewBox="0 0 24 24"><path d="M6 20v-6c0-3 2-5 4-5h1l1-4h3v5c2 1 3 3 3 5v5" fill="none" stroke="#2a7fa3" stroke-width="2"/></svg>
        <h3>Body Composition Analysis</h3>
        <p>Body analysis technology allows the practice to not only measure weight and body fat, it also provides muscle mass, body water, visceral fat, metabolic rate, age and physique.</p>
        <span class="btn btn-small">Read More</span>
      </div>
    </div>
    <div class="all"><span class="btn">See All Services</span></div>
  </div>
</section>

<section class="quiz" role="img" aria-label="Doctor at a desk behind a green tint">
  <h2>Are you toxic questionnaire?</h2>
  <p>Take our hormone quiz to find out if hormones are affecting your health.</p>
  <span class="btn">See Our All Questionnaire</span>
</section>

<section class="products">
  <div class="container">
    <div class="product-row">
      <div class="product"><div class="product-img" role="img" aria-label="Protein supplement box"></div><div class="name">Daily Greens Formula</div><div class="price">$40.00<s>$50.00</s></div></div>
      <div class="product"><div class="product-img" role="img" aria-label="Nutrition drink bottle"></div><div class="name">Daily Greens Formula</div><div class="price sale">$40.00<s>$50.00</s></div></div>
      <div class="product"><div class="product-img" role="img" aria-label="Supplement pill bottle"></div><div class="name">Daily Greens Formula</div><div class="price">$40.00</div></div>
      <div class="product"><div class="product-img" role="img" aria-label="Powder supplement tub"></div><div class="name">Daily Greens Formula</div><div class="price">$45.00</div></div>
    </div>
    <span class="btn">See More Products</span>
  </div>
  <span class="arrow prev"><svg width="10" height="10" viewBox="0 0 10 10"><path d="M6.5 1.5 3 5l3.5 3.5" fill="none" stroke="#fff" stroke-width="1.6"/></svg></span>
  <span class="arrow next"><svg width="10" height="10" viewBox="0 0 10 10"><path d="M3.5 1.5 7 5 3.5 8.5" fill="none" stroke="#fff" stroke-width="1.6"/></svg></span>
</section>

<section class="reviews" role="img" aria-label="Faded photo of a family outdoors">
  <div class="container">
    <h2 class="section-title">Clients Reviews</h2>
    <div class="avatar" role="img" aria-label="Client portrait"></div>
    <div class="reviewer">MORGAN HALE, LAWYER</div>
    <blockquote>Lorem Ipsum is simply dummy text of the printing and typesetting industry. Lorem Ipsum has been the industry's standard dummy text ever since the 1500s Lorem Ipsum is simply dummy text</blockquote>
    <div class="dots"><span></span><span class="on"></span><span></span><span></span><span></span><span></span><span></span><span></span><span></span><span></span><span></span></div>
  </div>
</section>

<section class="newsletter">
  <div>
    <h3>Newsleeter</h3>
    <p>Lorem Ipsum is simply dummy text of the printing and typesetting industry Lorem</p>
  </div>
  <div class="signup"><span>Your Email Address...</span><b>SUBSCRIBE</b></div>
</section>

<section class="blogs">
  <div class="container">
    <h2 class="section-title">From The Blogs</h2>
    <div class="blog-row">
      <article class="post">
        <div class="post-img" role="img" aria-label="Scientist working at a laboratory microscope" style="background:linear-gradient(135deg,#dbe7ef,#8fb3cc)"></div>
        <h4>Improving on Strategic Sourcing</h4>
        <div class="date"><svg width="9" height="9" viewBox="0 0 9 9"><rect x=".5" y="1.5" width="8" height="7" fill="none" stroke="#999"/></svg>December 2016, 10:26</div>
        <p>Lorem Ipsum is simply dummy text of the printing and typesetting industry. Lorem Ipsum has been the industry's Lorem Ipsum</p>
      </article>
      <article class="post">
        <div class="post-img" role="img" aria-label="Doctors discussing test results" style="background:linear-gradient(135deg,#e6edf2,#9ab6c9)"></div>
        <h4>Improving on Strategic Sourcing</h4>
        <div class="date"><svg width="9" height="9" viewBox="0 0 9 9"><rect x=".5" y="1.5" width="8" height="7" fill="none" stroke="#999"/></svg>December 2016, 10:26</div>
        <p>Lorem Ipsum is simply dummy text of the printing and typesetting industry. Lorem Ipsum has been the industry's Lorem Ipsum</p>
      </article>
      <article class="post">
        <div class="post-img" role="img" aria-label="Nurse in blue scrubs with stethoscope" style="background:linear-gradient(135deg,#eef2f5,#6f9ec4)"></div>
        <h4>Improving on Strategic Sourcing</h4>
        <div class="date"><svg width="9" height="9" viewBox="0 0 9 9"><rect x=".5" y="1.5" width="8" height="7" fill="none" stroke="#999"/></svg>December 2016, 10:26</div>
        <p>Lorem Ipsum is simply dummy text of the printing and typesetting industry. Lorem Ipsum has been the industry's Lorem Ipsum</p>
      </article>
    </div>
    <span class="btn">See All Blogs</span>
  </div>
</section>

<footer class="site-footer">
  <div class="container footer-grid">
    <div>
      <div class="footer-brand"><span class="brand-dot"></span>Bright Oak</div>
      <p class="footer-about">Lorem Ipsum is simply dummy text of the printing and typesetting industry. Lorem Ipsum has been the industry's standard dummy text</p>
      <div class="social"><span></span><span></span><span></span></div>
    </div>
    <div>
      <h4>Recent Posts</h4>
      <div class="recent"><i></i><div><b>Computer &amp; Table</b><small>By Admin</small></div></div>
      <div class="recent"><i></i><div><b>Computer &amp; Table</b><small>By Admin</small></div></div>
      <div class="recent"><i></i><div><b>Computer &amp; Table</b><small>By Admin</small></div></div>
    </div>
    <div>
      <h4>Contact us</h4>
      <ul class="contact">
        <li><svg width="9" height="11" viewBox="0 0 9 11"><path d="M4.5 10.5S1 6.5 1 4a3.5 3.5 0 0 1 7 0c0 2.5-3.5 6.5-3.5 6.5z" fill="none" stroke="#aaa"/></svg><span>1420 Oak Circle<br>Riverton, TX 75000</span></li>
        <li><svg width="9" height="9" viewBox="0 0 9 9"><path d="M1 1h2l1 2-1 1a5 5 0 0 0 2 2l1-1 2 1v2C4 8 1 5 1 1z" fill="none" stroke="#aaa"/></svg><span>(555) 010-4821</span></li>
        <li><svg width="10" height="8" viewBox="0 0 10 8"><rect x=".5" y=".5" width="9" height="7" fill="none" stroke="#aaa"/><path d="M.5.5 5 4l4.5-3.5" fill="none" stroke="#aaa"/></svg><span>(555) 010-7733</span></li>
      </ul>
    </div>
  </div>
</footer>
<div class="copyright">©2016 All Rights Reserved Bright Oak</div>

</body>
</html>
```